DELVANE ROOFING YARD SIGN

We need a yard sign to put in our customers' yards when we are roofing their home.
Delvane Roofing
468 Pettigrew Rd
Lake Charles LA 70452
phone: 337-555-0148

Maybe some verbiage like "Your Hometown Roofing Experts"
or
"Family Owned Since 1956"

```html
<!DOCTYPE html>
<html lang="en">
<head>
<meta charset="utf-8">
<title>Delvane Roofing Yard Sign</title>
<link href="https://fonts.googleapis.com/css2?family=Crimson+Pro:ital,wght@0,600;0,700;1,400;1,700&family=Poppins:wght@400;700&display=swap" rel="stylesheet">
<style>
  :root {
    --page: #e9e9e7;
    --ink: #0d0d0d;
    --paper: #ffffff;
    --shingle-dark: #111111;
    --shingle-mid: #2a2a2a;
    --silver-light: #f4f4f4;
    --silver-dark: #9a9a9a;
  }
  html, body {
    margin: 0;
    width: 1200px;
    height: 1200px;
    overflow: hidden;
    background: var(--page);
  }
  .canvas {
    width: 1200px;
    height: 1200px;
    display: flex;
    align-items: center;
    justify-content: center;
  }
  .yard-sign {
    width: 840px;
    height: 1120px;
    display: block;
    box-shadow: 0 10px 30px rgba(0,0,0,.18);
  }
  .brand-name {
    font-family: "Crimson Pro", Georgia, serif;
    font-weight: 700;
    fill: var(--paper);
  }
  .badge-name {
    font-family: "Crimson Pro", Georgia, serif;
    font-weight: 600;
    fill: var(--ink);
  }
  .tagline {
    font-family: "Crimson Pro", Georgia, serif;
    font-style: italic;
    font-weight: 400;
    fill: var(--ink);
  }
  .phone-number {
    font-family: "Poppins", Arial, sans-serif;
    font-weight: 700;
    fill: var(--ink);
  }
  .address {
    font-family: "Poppins", Arial, sans-serif;
    font-weight: 400;
    fill: var(--paper);
  }
  .heritage {
    font-family: "Crimson Pro", Georgia, serif;
    font-style: italic;
    font-weight: 700;
    fill: var(--ink);
  }
</style>
</head>
<body>
<main class="canvas">
  <svg class="yard-sign" viewBox="474 294 943 1258" xmlns="http://www.w3.org/2000/svg">
    <defs>
      <linearGradient id="shingleTone" x1="0" y1="0" x2="0" y2="1">
        <stop offset="0" stop-color="#1b1b1b"/>
        <stop offset="1" stop-color="#060606"/>
      </linearGradient>
      <linearGradient id="silverBand" x1="0" y1="0" x2="1" y2="0">
        <stop offset="0" stop-color="#bdbdbd"/>
        <stop offset=".5" stop-color="#f7f7f7"/>
        <stop offset="1" stop-color="#a8a8a8"/>
      </linearGradient>
      <linearGradient id="gableTone" x1="0" y1="0" x2="0" y2="1">
        <stop offset="0" stop-color="#3a3a3a"/>
        <stop offset=".25" stop-color="#0f0f0f"/>
        <stop offset="1" stop-color="#0b0b0b"/>
      </linearGradient>
    </defs>

    <!-- sign board -->
    <rect class="board" x="474" y="294" width="943" height="1258" fill="var(--paper)"/>

    <!-- roof shingles area -->
    <path class="roof-shingles" role="img" aria-label="Dark roof shingle texture"
          d="M474 294 H1417 V690 L1140 615 H760 L474 690 Z" fill="url(#shingleTone)"/>

    <!-- silver eave trim -->
    <path class="eave-trim" d="M474 690 L760 615 L760 640 L474 712 Z" fill="url(#silverBand)"/>
    <path class="eave-trim" d="M1140 615 L1417 690 L1417 712 L1140 640 Z" fill="url(#silverBand)"/>

    <!-- gable panel behind name -->
    <path class="name-gable" d="M533 782 L790 678 H1117 L1360 782 L1330 1165 H565 Z" fill="url(#gableTone)"/>

    <!-- name badge -->
    <circle class="badge-ring" cx="948" cy="580" r="192" fill="var(--paper)"/>
    <circle class="badge-edge" cx="948" cy="580" r="178" fill="none" stroke="#cfcfcf" stroke-width="3"/>
    <text class="badge-name" x="948" y="570" font-size="54" text-anchor="middle">Delvane</text>
    <text class="badge-name" x="948" y="628" font-size="54" text-anchor="middle">Roofing</text>

    <!-- company name -->
    <text class="brand-name" x="948" y="955" font-size="172" text-anchor="middle" textLength="670" lengthAdjust="spacingAndGlyphs">DELVANE</text>
    <text class="brand-name" x="948" y="1093" font-size="172" text-anchor="middle" textLength="670" lengthAdjust="spacingAndGlyphs">ROOFING</text>

    <!-- tagline -->
    <text class="tagline" x="946" y="1226" font-size="48" text-anchor="middle">Your Hometown Roofing Experts</text>

    <!-- phone -->
    <g class="phone-icon" transform="translate(610 1262)" fill="var(--ink)">
      <path d="M12 2 C8 2 2 6 2 12 C4 32 26 54 48 58 C54 58 58 52 58 48 L46 38 L38 44 C28 40 20 32 16 22 L22 14 Z"/>
      <path d="M34 4 A22 22 0 0 1 56 26" fill="none" stroke="var(--ink)" stroke-width="5" stroke-linecap="round"/>
      <path d="M34 16 A11 11 0 0 1 44 26" fill="none" stroke="var(--ink)" stroke-width="5" stroke-linecap="round"/>
    </g>
    <text class="phone-number" x="690" y="1318" font-size="80" textLength="590" lengthAdjust="spacingAndGlyphs">337-555-0148</text>

    <!-- address bar -->
    <rect class="address-bar" x="556" y="1361" width="774" height="112" fill="url(#silverBand)"/>
    <path class="address-panel" d="M556 1361 H1085 L1065 1473 H556 Z" fill="var(--ink)"/>
    <text class="address" x="620" y="1409" font-size="32">468 Pettigrew Rd</text>
    <text class="address" x="620" y="1447" font-size="32">Lake Charles LA 70452</text>
    <text class="heritage" x="1118" y="1410" font-size="29">Family Owned</text>
    <text class="heritage" x="1118" y="1443" font-size="29">Since 1956</text>
  </svg>
</main>
</body>
</html>
```